VelMarkory-Tagsworthly Partial Redesign - Web App

Are you able to apply your creativity to an existing layout? I’m convinced that even just a few touches can make a big difference to add personality and professionalism to a website design, and I’m looking for someone able to use existing ideas and bring them to the next level while keeping inside some given constraints.
The actual job is to improve an existing design concept and to apply it creatively to a landing page, a simple home page, and an older web app (single page website).
To help you start with a clear picture of the current situation and of my requirements, I created a detailed brief with screenshots, live examples, and complete instructions. You can find it attached to this job.
My tastes are inclined towards clean and simple designs. For this project I'm not looking for dazzling novelty, but for very solid craftsmanship. Are the right man - or woman - for the job?
Updates
I wanted to thank everybody who participated in this project. I made a choice, but also other designs were interesting. Hope to work with you another time.
Target Market(s)
Our main target is social media marketers and startuppers
Look and feel
Each slider illustrates characteristics of the customer's brand and the style your logo design should communicate.

```html
<!DOCTYPE html>
<html lang="en">
<head>
<meta charset="utf-8">
<title>VelMarkory – Hash tag</title>
<link rel="stylesheet" href="https://fonts.googleapis.com/css2?family=PT+Sans:wght@400;700&display=swap">
<style>
  :root {
    --ink: #333333;
    --ink-soft: #555555;
    --nav-bg: #3a3d44;
    --accent: #e0401a;
    --sky: #1aa6dc;
    --sky-light: #2bb8ea;
    --panel: #f2f2f2;
    --line: #d6d6d6;
    --chart-blue: #3366cc;
    --chart-red: #dc3912;
    --gauge-orange: #ff9900;
    --gauge-green: #109618;
    --footer-bg: #3a3d44;
  }
  * { box-sizing: border-box; margin: 0; padding: 0; }
  html, body { width: 1191px; height: 1200px; overflow: hidden; background: #fff; }
  body { font-family: "PT Sans", sans-serif; color: var(--ink); position: relative; }

  .site-header { position: absolute; left: 0; top: 0; width: 1191px; height: 109px; }
  .brand { position: absolute; left: 149px; top: 30px; display: flex; align-items: center; gap: 12px; }
  .brand-mark { width: 40px; height: 40px; border-radius: 50%; background: #4a4a4a; }
  .brand-name { font-size: 34px; font-weight: 700; color: #4a4a4a; letter-spacing: -0.5px; }
  .counter { position: absolute; top: 40px; display: flex; align-items: center; gap: 4px; }
  .counter-dot { width: 28px; height: 28px; border-radius: 50%; }
  .counter-dot.blue-light { background: #33bbee; }
  .counter-dot.blue-dark { background: #3b5a98; }
  .counter-value { background: #ececec; border: 1px solid #dcdcdc; font-size: 13px; padding: 3px 7px; }

  .main-nav { position: absolute; left: 0; top: 109px; width: 1191px; height: 33px; background: var(--nav-bg); }
  .main-nav a { position: absolute; top: 0; height: 33px; line-height: 33px; color: #fff; font-size: 13px; font-weight: 700; text-decoration: none; }
  .main-nav a.active { background: var(--accent); width: 95px; text-align: center; }

  .sub-tabs { position: absolute; left: 149px; top: 151px; width: 326px; height: 33px; border-radius: 3px; overflow: hidden; display: flex; background: #3a3d44; }
  .sub-tabs span { color: #fff; font-size: 13px; line-height: 33px; text-align: center; }
  .sub-tabs .current { width: 164px; background: linear-gradient(#6a6d73, #4b4e55); color: #e6e6e6; }
  .sub-tabs .other { flex: 1; }
  .goto { position: absolute; left: 978px; top: 152px; width: 62px; height: 29px; border: 1px solid #ccc; background: linear-gradient(#fafafa, #e6e6e6); font-size: 12px; font-weight: 700; color: #555; line-height: 27px; padding-left: 8px; }
  .goto::after { content: ""; position: absolute; right: 7px; top: 10px; border: 5px solid transparent; border-top: 7px solid #999; }
  .divider { position: absolute; left: 149px; top: 199px; width: 892px; height: 2px; background: #e6e6e6; }

  .stat { position: absolute; top: 216px; height: 76px; text-align: center; border: 1px solid #d8d8d8; background: linear-gradient(#fbfbfb, #e9e9e9); }
  .stat.highlight { background: linear-gradient(var(--sky-light), var(--sky)); border-color: var(--sky); color: #fff; }
  .stat-value { font-size: 29px; line-height: 1; margin-top: 13px; color: #555; }
  .stat.highlight .stat-value, .stat.highlight .stat-label { color: #fff; }
  .stat-label { font-size: 13px; color: #555; margin-top: 2px; }

  .section-bar { position: absolute; left: 148px; width: 894px; height: 39px; border: 1px solid #d6d6d6; background: linear-gradient(#f7f7f7, #e4e4e4); text-align: center; font-size: 16px; font-weight: 700; line-height: 38px; color: #333; }

  .chart-title { position: absolute; font-size: 15px; font-weight: 700; color: #444; display: flex; align-items: center; gap: 6px; letter-spacing: 0.3px; }
  .marker { display: inline-block; width: 5px; height: 20px; border-radius: 3px; }
  .marker.red { background: var(--chart-red); }
  .marker.blue { background: #2a8ae0; }
  .markers { display: inline-flex; gap: 14px; margin-left: 4px; }

  .gauge { position: absolute; width: 260px; height: 260px; }
  .pie { position: absolute; width: 170px; height: 170px; }
  .legend { position: absolute; font-size: 10px; color: #222; line-height: 13px; }
  .legend-row { display: flex; gap: 5px; margin-bottom: 5px; }
  .legend-swatch { width: 10px; height: 10px; flex: none; margin-top: 1px; }

  .site-footer { position: absolute; left: 0; top: 1158px; width: 1191px; height: 42px; background: var(--footer-bg); color: #bbb; font-size: 11px; }
  .copyright { position: absolute; left: 149px; top: 14px; }
  .footer-links { position: absolute; right: 152px; top: 14px; }
  .social-squares { position: absolute; left: 566px; top: 12px; display: flex; gap: 4px; }
  .social-squares span { width: 17px; height: 17px; border-radius: 2px; }
</style>
</head>
<body>

<header class="site-header">
  <div class="brand"><span class="brand-mark"></span><span class="brand-name">VelMarkory</span></div>
  <div class="counter" style="left:772px"><span class="counter-dot blue-light"></span><span class="counter-value">336,365</span></div>
  <div class="counter" style="left:902px"><span class="counter-dot blue-dark"></span><span class="counter-value">336,365</span></div>
</header>

<nav class="main-nav">
  <a style="left:180px">About</a>
  <a style="left:276px">Summary</a>
  <a style="left:390px">Time line</a>
  <a style="left:506px">Influencers</a>
  <a class="active" style="left:603px">Hash tag</a>
  <a style="left:734px">Blog</a>
</nav>

<div class="sub-tabs"><span class="current">Tracked Hashtags</span><span class="other">Hashtags Explore</span></div>
<div class="goto">GOTO</div>
<div class="divider"></div>

<div class="stat" style="left:153px;width:170px"><div class="stat-value">8</div><div class="stat-label">Observed Days</div></div>
<div class="stat highlight" style="left:333px;width:168px"><div class="stat-value">8,492,949</div><div class="stat-label">Total impression</div></div>
<div class="stat highlight" style="left:511px;width:168px"><div class="stat-value">843</div><div class="stat-label">Total Tweets</div></div>
<div class="stat" style="left:689px;width:169px"><div class="stat-value">1,061,619</div><div class="stat-label">Daily Impression</div></div>
<div class="stat" style="left:868px;width:169px"><div class="stat-value">105</div><div class="stat-label">Daily Tweets</div></div>

<div class="section-bar" style="top:326px">YOUR INFLUENCERS ANALYSIS</div>

<div class="chart-title" style="left:236px;top:422px">Trend With Your Influencers
  <span class="markers"><span class="marker red"></span><span class="marker red"></span><span class="marker blue"></span></span></div>
<div class="chart-title" style="left:670px;top:422px">Trend Without Your Influencers
  <span class="markers"><span class="marker red"></span><span class="marker red"></span></span></div>

<svg class="gauge" style="left:234px;top:466px" viewBox="-130 -130 260 260" aria-label="Trend gauge with influencers, value 3">
  <circle r="124" fill="#c8c8c8" stroke="#999" stroke-width="1"/>
  <circle r="115" fill="#f6f6f6" stroke="#e2e2e2" stroke-width="2"/>
  <path d="M -67.2 67.2 A 95 95 0 0 1 -43.1 -84.6" fill="none" stroke="var(--chart-red)" stroke-width="24"/>
  <path d="M -43.1 -84.6 A 95 95 0 0 1 43.1 -84.6" fill="none" stroke="var(--gauge-orange)" stroke-width="24"/>
  <path d="M 43.1 -84.6 A 95 95 0 0 1 67.2 67.2" fill="none" stroke="var(--gauge-green)" stroke-width="24"/>
  <g stroke="#333" stroke-width="2">
    <line x1="-74.2" y1="74.2" x2="-59.4" y2="59.4"/><line x1="-97" y1="-40.2" x2="-77.6" y2="-32.1"/>
    <line x1="0" y1="-105" x2="0" y2="-84"/><line x1="97" y1="-40.2" x2="77.6" y2="-32.1"/>
    <line x1="74.2" y1="74.2" x2="59.4" y2="59.4"/>
  </g>
  <text x="0" y="-28" text-anchor="middle" font-size="28" fill="#333" font-family="PT Sans, sans-serif">Trend</text>
  <text x="-40" y="60" text-anchor="middle" font-size="14" fill="#333" font-family="PT Sans, sans-serif">-100</text>
  <text x="43" y="60" text-anchor="middle" font-size="14" fill="#333" font-family="PT Sans, sans-serif">100</text>
  <text x="0" y="95" text-anchor="middle" font-size="26" fill="#111" font-family="PT Sans, sans-serif">3</text>
  <g transform="rotate(4)"><path d="M0,-92 L4,0 L0,32 L-4,0Z" fill="#e9694d" stroke="#c4452a" stroke-width="1"/></g>
  <circle r="15" fill="#4a86e8" stroke="#3a6fc4" stroke-width="1"/>
</svg>

<svg class="gauge" style="left:668px;top:466px" viewBox="-130 -130 260 260" aria-label="Trend gauge without influencers, value 3">
  <circle r="124" fill="#c8c8c8" stroke="#999" stroke-width="1"/>
  <circle r="115" fill="#f6f6f6" stroke="#e2e2e2" stroke-width="2"/>
  <path d="M -67.2 67.2 A 95 95 0 0 1 -43.1 -84.6" fill="none" stroke="var(--chart-red)" stroke-width="24"/>
  <path d="M -43.1 -84.6 A 95 95 0 0 1 43.1 -84.6" fill="none" stroke="var(--gauge-orange)" stroke-width="24"/>
  <path d="M 43.1 -84.6 A 95 95 0 0 1 67.2 67.2" fill="none" stroke="var(--gauge-green)" stroke-width="24"/>
  <g stroke="#333" stroke-width="2">
    <line x1="-74.2" y1="74.2" x2="-59.4" y2="59.4"/><line x1="-97" y1="-40.2" x2="-77.6" y2="-32.1"/>
    <line x1="0" y1="-105" x2="0" y2="-84"/><line x1="97" y1="-40.2" x2="77.6" y2="-32.1"/>
    <line x1="74.2" y1="74.2" x2="59.4" y2="59.4"/>
  </g>
  <text x="0" y="-28" text-anchor="middle" font-size="28" fill="#333" font-family="PT Sans, sans-serif">Trend</text>
  <text x="-40" y="60" text-anchor="middle" font-size="14" fill="#333" font-family="PT Sans, sans-serif">-100</text>
  <text x="43" y="60" text-anchor="middle" font-size="14" fill="#333" font-family="PT Sans, sans-serif">100</text>
  <text x="0" y="95" text-anchor="middle" font-size="26" fill="#111" font-family="PT Sans, sans-serif">3</text>
  <g transform="rotate(4)"><path d="M0,-92 L4,0 L0,32 L-4,0Z" fill="#e9694d" stroke="#c4452a" stroke-width="1"/></g>
  <circle r="15" fill="#4a86e8" stroke="#3a6fc4" stroke-width="1"/>
</svg>

<div class="section-bar" style="top:773px">YOUR INFLUENCERS ANALYSIS</div>

<div class="chart-title" style="left:215px;top:874px">Your Influencers <span class="marker blue"></span> vs Rest Of The Internet
  <span class="markers"><span class="marker red"></span><span class="marker red"></span></span></div>
<div class="chart-title" style="left:673px;top:874px">Your Influencers <span class="marker blue"></span> vs Your Influencers <span class="marker blue"></span></div>

<svg class="pie" style="left:298px;top:929px" viewBox="-85 -85 170 170" aria-label="Pie chart: tracked influencers 14.9%, others 85.1%">
  <path d="M0,0 L64.4,-47.5 A80 80 0 1 1 0 -80 Z" fill="var(--chart-red)" stroke="#fff" stroke-width="1"/>
  <path d="M0,0 L0,-80 A80 80 0 0 1 64.4 -47.5 Z" fill="var(--chart-blue)" stroke="#fff" stroke-width="1"/>
  <text x="27" y="-49" text-anchor="middle" font-size="10" fill="#fff" font-family="PT Sans, sans-serif">14.9%</text>
  <text x="-29" y="56" text-anchor="middle" font-size="10" fill="#fff" font-family="PT Sans, sans-serif">85.1%</text>
</svg>
<div class="legend" style="left:480px;top:927px">
  <div class="legend-row"><span class="legend-swatch" style="background:var(--chart-blue)"></span><span>Tracked<br>Influencers</span></div>
  <div class="legend-row"><span class="legend-swatch" style="background:var(--chart-red)"></span><span>Others</span></div>
</div>

<svg class="pie" style="left:732px;top:929px" viewBox="-85 -85 170 170" aria-label="Pie chart: lunarfox 8.1%, petergrayl 91.9%">
  <path d="M0,0 L39,-69.8 A80 80 0 1 1 0 -80 Z" fill="var(--chart-red)" stroke="#fff" stroke-width="1"/>
  <path d="M0,0 L0,-80 A80 80 0 0 1 39 -69.8 Z" fill="var(--chart-blue)" stroke="#fff" stroke-width="1"/>
  <text x="15" y="-55" text-anchor="middle" font-size="10" fill="#fff" font-family="PT Sans, sans-serif">8.1%</text>
  <text x="-15" y="60" text-anchor="middle" font-size="10" fill="#fff" font-family="PT Sans, sans-serif">91.9%</text>
</svg>
<div class="legend" style="left:914px;top:927px">
  <div class="legend-row"><span class="legend-swatch" style="background:var(--chart-blue)"></span><span>lunarfox...</span></div>
  <div class="legend-row"><span class="legend-swatch" style="background:var(--chart-red)"></span><span>petergrayl</span></div>
</div>

<footer class="site-footer">
  <span class="copyright">© 2012. VelMarkory Ltd. All Rights Reserved.</span>
  <div class="social-squares">
    <span style="background:#3b5a98"></span><span style="background:#33bbee"></span><span style="background:#1a7ab8"></span><span style="background:#333"></span><span style="background:#f28a1e"></span>
  </div>
  <span class="footer-links">Privacy Policy | T&amp;C</span>
</footer>

</body>
</html>
```